A5 Personal trainer profile for corbell vitality

I need a A5 Landscape profile designed for the company I work for. Company name is Corbell Vitality. The profile is for personal trainers to let people know:

1. Brief description of themselves
2. Qualifications

A picture will be required on the right hand side of the profile. Corbell Vitality colours are green and white.

The Corbell Vitality Logo in the boarder of the example included must remain. We are looking for a clinical and professional design.

Industry/Entity Type

Health

```html
<!DOCTYPE html>
<html lang="en">
<head>
<meta charset="utf-8">
<title>Corbell Vitality – Personal Trainer Profile</title>
<link rel="stylesheet" href="https://fonts.googleapis.com/css2?family=Alfa+Slab+One&family=Arimo:wght@400;700&display=swap">
<style>
  :root {
    --paper: #f7f8f7;
    --frame: #ffffff;
    --photo-deep: #24403a;
    --photo-mid: #4d6a58;
    --photo-light: #8fa79a;
    --photo-skin: #b79a80;
    --photo-blue: #2f87b5;
    --ink-white: #ffffff;
    --brand-green: #2d7a2e;
    --body-ink: #25302a;
  }
  * { margin: 0; padding: 0; box-sizing: border-box; }
  html, body { width: 1200px; height: 849px; overflow: hidden; background: var(--paper); }
  .profile {
    position: relative;
    width: 1200px;
    height: 849px;
    background:
      radial-gradient(ellipse at 20% 95%, rgba(160,170,165,.18), transparent 60%),
      var(--paper);
    font-family: "Arimo", Arial, sans-serif;
    overflow: hidden;
  }
  .photo-frame { position: absolute; inset: 0; width: 1200px; height: 849px; }
  .headline, .title-block {
    position: absolute;
    font-family: "Alfa Slab One", Georgia, serif;
    color: var(--ink-white);
    text-transform: uppercase;
    letter-spacing: 4px;
    line-height: 1;
    text-shadow: 0 0 2px rgba(255,255,255,.5);
    opacity: .93;
  }
  .headline { left: 92px; top: 38px; font-size: 66px; line-height: 62px; transform: rotate(2deg); transform-origin: left top; }
  .brand-plate {
    position: absolute; left: 515px; top: 166px; width: 618px; height: 70px;
    background: var(--frame);
    display: flex; align-items: center; gap: 16px; padding-left: 10px;
  }
  .brand-mark { width: 50px; height: 50px; background: var(--brand-green); }
  .brand-name { font-family: "Arimo", Arial, sans-serif; font-weight: 700; font-size: 60px; color: var(--brand-green); letter-spacing: -1px; }
  .service-list, .qualifications {
    position: absolute; list-style: none;
    color: var(--ink-white); font-size: 24px; line-height: 34px;
    text-shadow: 0 1px 3px rgba(0,0,0,.75);
  }
  .service-list { left: 88px; top: 172px; width: 370px; }
  .service-list li::before, .qualifications li::before { content: "•"; }
  .qualifications { left: 562px; top: 248px; width: 543px; text-align: justify; }
  .qualifications .heading { font-weight: 700; }
  .qualifications .heading::before { content: none; }
  .title-block { font-size: 50px; letter-spacing: 3px; }
  .title-role { left: 367px; top: 554px; }
  .title-name { left: 625px; top: 598px; width: 490px; text-align: right; }
  .testimonial { position: absolute; left: 78px; top: 680px; width: 1060px; color: var(--body-ink); font-size: 20.5px; line-height: 34px; }
  .testimonial h2 { font-size: 20.5px; font-weight: 700; line-height: 28px; }
  .testimonial p { line-height: 33px; }
  .testimonial .client { font-weight: 700; }
</style>
</head>
<body>
<main class="profile">
  <svg class="photo-frame" viewBox="0 0 1200 849" aria-hidden="false">
    <defs>
      <linearGradient id="gymTone" x1="0" y1="0" x2="1" y2="1">
        <stop offset="0" stop-color="#9fb3a8"/>
        <stop offset=".3" stop-color="#4d6a58"/>
        <stop offset=".65" stop-color="#2c4a42"/>
        <stop offset="1" stop-color="#1f3833"/>
      </linearGradient>
      <radialGradient id="leftFigure" cx=".33" cy=".35" r=".28">
        <stop offset="0" stop-color="#b79a80" stop-opacity=".75"/>
        <stop offset="1" stop-color="#b79a80" stop-opacity="0"/>
      </radialGradient>
      <radialGradient id="rightFigure" cx=".72" cy=".45" r=".3">
        <stop offset="0" stop-color="#2f87b5" stop-opacity=".8"/>
        <stop offset="1" stop-color="#2f87b5" stop-opacity="0"/>
      </radialGradient>
    </defs>
    <polygon points="40,0 1182,0 1174,744 36,612" fill="#ffffff"/>
    <g role="img" aria-label="Photograph of two personal trainers working out in a gym, one in a green vest and one in a blue top">
      <polygon points="58,0 1162,0 1156,724 55,594" fill="url(#gymTone)"/>
      <polygon points="58,0 1162,0 1156,724 55,594" fill="url(#leftFigure)"/>
      <polygon points="58,0 1162,0 1156,724 55,594" fill="url(#rightFigure)"/>
    </g>
  </svg>

  <h1 class="headline">How I can<br>help you?</h1>

  <div class="brand-plate">
    <span class="brand-mark"></span>
    <span class="brand-name">Corbell Vitality</span>
  </div>

  <ul class="service-list">
    <li>Reduce body fat and increase body definition</li>
    <li>Increase stamina, improve agility and speed</li>
    <li>Increase strength and size</li>
    <li>Plyometric training and conditioning</li>
    <li>Flexibility and core strength</li>
  </ul>

  <ul class="qualifications">
    <li class="heading">Qualifications</li>
    <li>Advanced Circuit Training</li>
    <li>Advanced Diploma in Personal Training - Level 3 EPRS Registered</li>
    <li>Fitness Instructor - Level 2 EPRS Registered</li>
    <li>Also qualified in – Suspension training, Studio Cycling, Sports Nutrition, Weight Management</li>
  </ul>

  <div class="title-block title-role">Personal Trainer</div>
  <div class="title-block title-name">Marcus Ottley</div>

  <section class="testimonial">
    <h2>What my clients say about me?</h2>
    <p>&nbsp;"With Marcus my training is always challenging and fun.<br>
    I don’t remember a session to be boring or repetitive. In short time I improved my core strength<br>
    and flexibility. I can run 10k without stopping. It is amazing improvement.&nbsp; " ~ <span class="client">Rachel Denholm</span></p>
  </section>
</main>
</body>
</html>
```